Author requires ebook cover for sweet romance novel

The first of a sweet romance trilogy that will be uploaded to Brindlemart in ebook form. Would love to get a bright and light cover to attract readers.
Author name: Tessa Holloway . Would prefer this in the upper section of the cover.
Book title: Rosalind's Promise. The Harvest Saga Book 1.
Main character Rosalind: 32 year old woman with blue eyes and long, wavy auburn/red hair. Caucasian. Doctor. Sophisticated with understated sex appeal.
Setting: Australian Outback . Photos of Warrabin/Tollard Crag acceptable or any red/orange dirt outback photo
The chosen designer will immediately receive a request for two further ebook covers. For ongoing work the author expects to have a trilogy ready for publishing every four months or less.
Requirements
Must have
- See attached doc
Should not have
- illustrations

```html
<!DOCTYPE html>
<html lang="en">
<head>
<meta charset="utf-8">
<title>Rosalind's Promise — Ebook Cover</title>
<link rel="stylesheet" href="https://fonts.googleapis.com/css2?family=Cinzel:wght@400;500;600&family=Great+Vibes&display=swap">
<style>
  :root {
    --page-bg: #ffffff;
    --author-orange: #f59a12;
    --title-orange: #e8641c;
    --title-purple: #7a2fc4;
    --series-white: #fff8ec;
    --sky-light: #f1eee8;
    --sky-mid: #e4dfd6;
    --treeline: #8f9077;
    --haze: #e9e4da;
    --hair-red: #c9502a;
    --denim-grey: #8d95a0;
    --scrub-green: #7f8f3e;
    --grass-gold: #d8b848;
    --sand-orange: #eb902e;
    --sand-deep: #dc7420;
  }
  * { margin: 0; padding: 0; box-sizing: border-box; }
  html, body {
    width: 1200px;
    height: 1200px;
    overflow: hidden;
    background: var(--page-bg);
  }
  .canvas {
    position: relative;
    width: 1200px;
    height: 1200px;
  }
  .cover {
    position: absolute;
    left: 230px;
    top: 45px;
    width: 740px;
    height: 1110px;
    overflow: hidden;
  }
  .cover-photo {
    position: absolute;
    inset: 0;
    width: 100%;
    height: 100%;
    display: block;
  }
  .author-name {
    position: absolute;
    top: 38px;
    left: 0;
    right: 0;
    text-align: center;
    font-family: "Cinzel", serif;
    font-weight: 500;
    font-size: 66px;
    letter-spacing: 2px;
    color: var(--author-orange);
    white-space: nowrap;
  }
  .title {
    position: absolute;
    top: 470px;
    left: 0;
    right: 0;
    text-align: center;
    font-weight: normal;
  }
  .title-script {
    display: block;
    font-family: "Great Vibes", cursive;
    font-size: 158px;
    line-height: 1;
    color: var(--title-orange);
    white-space: nowrap;
  }
  .title-caps {
    display: block;
    margin-top: 4px;
    font-family: "Cinzel", serif;
    font-weight: 600;
    font-size: 84px;
    letter-spacing: 2px;
    color: var(--title-purple);
  }
  .series {
    position: absolute;
    top: 952px;
    left: 0;
    right: 0;
    text-align: center;
    font-family: "Cinzel", serif;
    font-weight: 400;
    font-size: 34px;
    line-height: 1.42;
    color: var(--series-white);
  }
</style>
</head>
<body>
<main class="canvas">
  <section class="cover">
    <svg class="cover-photo" viewBox="0 0 740 1110" preserveAspectRatio="none" role="img" aria-label="Photograph of a red-haired woman in a denim jacket, hair blowing across her face, blended over an Australian outback scene: pale overcast sky, distant tree line, green scrub and a path of orange sand">
      <defs>
        <linearGradient id="landscape" x1="0" y1="0" x2="0" y2="1">
          <stop offset="0" stop-color="var(--sky-light)"/>
          <stop offset="0.26" stop-color="var(--sky-mid)"/>
          <stop offset="0.32" stop-color="#b9b59f"/>
          <stop offset="0.37" stop-color="var(--treeline)"/>
          <stop offset="0.43" stop-color="#b7a68e"/>
          <stop offset="0.53" stop-color="var(--haze)"/>
          <stop offset="0.58" stop-color="#dfdccb"/>
          <stop offset="0.61" stop-color="#b5b55e"/>
          <stop offset="0.66" stop-color="var(--grass-gold)"/>
          <stop offset="0.74" stop-color="#eda33c"/>
          <stop offset="0.87" stop-color="var(--sand-orange)"/>
          <stop offset="1" stop-color="var(--sand-deep)"/>
        </linearGradient>
        <radialGradient id="hair" cx="0.5" cy="0.5" r="0.5">
          <stop offset="0" stop-color="var(--hair-red)" stop-opacity="0.95"/>
          <stop offset="0.55" stop-color="var(--hair-red)" stop-opacity="0.7"/>
          <stop offset="1" stop-color="var(--hair-red)" stop-opacity="0"/>
        </radialGradient>
        <radialGradient id="jacket" cx="0.5" cy="0.5" r="0.5">
          <stop offset="0" stop-color="var(--denim-grey)" stop-opacity="0.55"/>
          <stop offset="1" stop-color="var(--denim-grey)" stop-opacity="0"/>
        </radialGradient>
        <radialGradient id="scrub" cx="0.5" cy="0.5" r="0.5">
          <stop offset="0" stop-color="var(--scrub-green)" stop-opacity="0.85"/>
          <stop offset="1" stop-color="var(--scrub-green)" stop-opacity="0"/>
        </radialGradient>
        <radialGradient id="path" cx="0.5" cy="0.5" r="0.5">
          <stop offset="0" stop-color="#f4a640" stop-opacity="0.8"/>
          <stop offset="1" stop-color="#f4a640" stop-opacity="0"/>
        </radialGradient>
      </defs>
      <rect width="740" height="1110" fill="url(#landscape)"/>
      <ellipse cx="360" cy="560" rx="280" ry="170" fill="url(#jacket)"/>
      <ellipse cx="330" cy="300" rx="330" ry="190" fill="url(#hair)"/>
      <ellipse cx="390" cy="430" rx="220" ry="130" fill="url(#hair)" opacity="0.6"/>
      <ellipse cx="60" cy="900" rx="230" ry="260" fill="url(#scrub)"/>
      <ellipse cx="700" cy="820" rx="170" ry="260" fill="url(#scrub)"/>
      <ellipse cx="400" cy="960" rx="260" ry="200" fill="url(#path)"/>
    </svg>

    <p class="author-name">TESSA HOLLOWAY</p>

    <h1 class="title">
      <span class="title-script">Rosalind's</span>
      <span class="title-caps">Promise</span>
    </h1>

    <p class="series">The Harvest Saga<br>Book 1</p>
  </section>
</main>
</body>
</html>
```